Flyer needed For the Council for Stewardship of Public Works

With an increasing need for professional staffing in our design and construction industry it is important for organizations to be able to attract, support, and retain people of all genders. With the increase of women entering the design/construction industry, we need to be able to identify and address the specific needs of women in our industry, including those A/E’s who are on the facility Owner side.

This Forum will provide a venue to openly discuss the issues affecting our industry and ideas to address those issues.The program includes time for presentations and a panel discussion by accomplished women in our industry, and facilitated table and open discussions to form solutions with your peers. You will come away with ideas you can implement within your organization to build processes and a supportive culture for women

IN THE ATTACHMENTS
* you'll find our company logo

Target Market(s)

Women in the design and construction industry

Industry/Entity Type

Construction

Requirements
Must have
• Logo, event name, date, time, location, panelists names and pics, NBF continuing education provided, contact information: Maren Holtzclaw, maren.holtzclaw@c-sfpw.org, (555) 740-1938
• Register at: www.c-sfpw.org/events
• Design should encompass the description given above.
Nice to have
• Colors that compliment our logo

```html
<!DOCTYPE html>
<html lang="en">
<head>
<meta charset="utf-8">
<title>AEC Industry Women's Mini-Forum &amp; Workshop</title>
<link rel="stylesheet" href="https://fonts.googleapis.com/css2?family=Carlito:ital,wght@0,400;0,700;1,400&display=swap">
<style>
:root{
  --navy:#2f2a6e;
  --blue:#2b6cb3;
  --sky:#e1eef9;
  --sky-deep:#c7dcef;
  --ink:#1d1d1d;
  --line:#3a3a3a;
  --green:#8dbb4a;
  --paper:#ffffff;
}
*{margin:0;padding:0;box-sizing:border-box}
html,body{width:859px;height:1200px;overflow:hidden;background:var(--paper)}
body{font-family:"Carlito",Calibri,Arial,sans-serif;color:var(--ink);position:relative}
.brand{position:absolute;left:22px;top:18px;display:flex;align-items:center;gap:14px}
.brand-dot{width:58px;height:58px;background:var(--navy);border-radius:4px}
.brand-name{font-size:44px;font-weight:700;color:var(--navy);line-height:1}
.brand-sub{font-size:14px;color:var(--navy);margin-top:4px}
.partner-badge{position:absolute;right:22px;top:12px;width:110px;height:110px;border-radius:50%;background:var(--sky-deep)}
.event-title{position:absolute;left:20px;right:20px;top:134px;text-align:center;font-size:31px;line-height:1.1;font-weight:700;color:var(--navy);white-space:nowrap}
.side{position:absolute;left:0;top:190px;width:185px;padding-left:18px;border-right:3px solid var(--green);height:960px}
.side h2{font-size:34px;font-weight:700;color:var(--blue);line-height:1}
.side .detail{font-size:19px;color:var(--navy);font-weight:700;margin:12px 0 50px}
.timing{list-style:none;margin-top:10px}
.timing li{font-size:16px;line-height:1.2;margin-bottom:14px;color:var(--ink)}
.timing b{color:var(--blue)}
.main{position:absolute;left:205px;top:182px;width:636px;height:740px;background:linear-gradient(180deg,var(--sky) 0%,#f3f8fd 100%);display:flex;flex-direction:column}
.main-visual{position:absolute;right:0;top:0;width:260px;height:300px;background:linear-gradient(160deg,#cfe0f0,#eef5fb);opacity:.7}
.intro{position:relative;padding:16px 22px 0;font-size:17.5px;line-height:1.28}
.intro strong{font-weight:700}
.roles{position:relative;padding:16px 22px 0;font-size:18px;line-height:1.25}
.roles b{font-size:21px;color:var(--navy)}
.cast{position:relative;margin:18px 22px 0;display:flex;gap:14px}
.cast-box{border:2px solid var(--line);background:#fff;padding:10px 12px;font-size:16.5px;line-height:1.25;flex:1}
.cast-box ul{list-style:none}
.cast-box li{margin-bottom:8px;padding-left:16px;position:relative}
.cast-box li::before{content:"";position:absolute;left:0;top:7px;width:7px;height:7px;background:var(--navy);border-radius:50%}
.cast-box b{font-weight:700}
.contact{position:absolute;left:320px;top:945px;width:470px;background:var(--sky);border:2px solid var(--sky-deep);padding:14px 20px;text-align:center;font-size:19px;color:var(--blue);line-height:1.3}
.contact b{font-weight:700}
.register{font-size:24px;font-weight:700;margin-top:6px}
.ce{position:absolute;left:320px;top:1095px;width:470px;text-align:center;font-size:18px;color:var(--navy);font-weight:700}
</style>
</head>
<body>
<header class="brand">
  <span class="brand-dot"></span>
  <div>
    <div class="brand-name">C-SfPW</div>
    <div class="brand-sub">Council for Stewardship of Public Works</div>
  </div>
</header>
<div class="partner-badge" aria-hidden="true"></div>

<h1 class="event-title">AEC Industry women’s Mini-Forum &amp; Workshop</h1>

<aside class="side">
  <h2>DATE</h2>
  <p class="detail">January 13, 2016</p>
  <h2>LOCATION</h2>
  <p class="detail">Riverbend Conference Suites, Millbrook, Texas</p>
  <h2>PROGRAM TIMING</h2>
  <ul class="timing">
    <li><b>1:00</b>, Registration and Networking (refreshments)</li>
    <li><b>1:30, Program:</b></li>
    <li><b>1:30</b>, Welcome and introduce panel moderator (Dana Pellerin)</li>
    <li><b>1:40</b>, Presentations</li>
    <li><b>2:30</b>, Panel/Q&amp;A</li>
    <li><b>3:20</b>, Break (refreshments)</li>
    <li><b>3:40</b> Table discussions - facilitated; focus on ideas to address issues</li>
    <li><b>4:10</b>, Report out and open discussion - solutions!</li>
    <li><b>4:45</b>, Conclusions, Closing</li>
    <li><b>4:45</b>, Adjourn</li>
  </ul>
</aside>

<main class="main">
  <div class="main-visual" role="img" aria-label="Soft faded view of a building under construction"></div>
  <p class="intro">With an increasing need for professional staffing in our design and construction industry it is important for organizations to be able to attract, support, and retain people of all genders. With the increase of women entering the design/construction industry, we need to be able to identify and address the specific needs of women in our industry, including those A/E’s who are on the facility Owner side. This Forum will provide a venue to openly discuss the issues affecting our industry and ideas to address those issues. The program includes time for presentations and a panel discussion by accomplished women in our industry, and facilitated table and open discussions to form solutions with your peers. <strong>You will come away with ideas you can implement within your organization to build processes and a supportive culture for women.</strong> A visual note-taker and separate scribe will be utilized to compile ideas and solutions, for distribution to participants after the event.</p>
  <p class="roles"><b>Presenters and Panelists:</b> architect, engineer, contractor, subtrade, facility Owner<br><b>Table Facilitators:</b> one for each table, with tables divided into industry segments: architects, engineers, contractors, subs/trades, Owners</p>
  <div class="cast">
    <div class="cast-box">
      <ul>
        <li><b>Master of Ceremonies:</b><br>Dana Pellerin</li>
        <li><b>Scribe:</b> Maren Holtzclaw</li>
        <li><b>Visual Note Taking:</b><br>Tessa Marlow<br>marlowsketch.net/connect</li>
        <li><b>Panel:</b> Moderator – Joan Ferrante (Keystone Builders)</li>
      </ul>
    </div>
    <div class="cast-box">
      <ul>
        <li><b>Architect:</b> Lorne Vale Architects</li>
        <li><b>Engineer:</b> Brightwater Engineering</li>
        <li><b>Contractor:</b> Rosa Delvecchio (Delvecchio Builders)</li>
        <li><b>Owner:</b> Ines Okafor (State Facilities Office)</li>
        <li><b>Sub-trade:</b></li>
      </ul>
    </div>
  </div>
</main>

<section class="contact">
  <p><b>Contact Information:</b> Maren Holtzclaw,<br>maren.holtzclaw@c-sfpw.org<br>(555) 740-1938</p>
  <p class="register">Register at: www.c-sfpw.org/events</p>
</section>
<p class="ce">NBF continuing education provided</p>
</body>
</html>
```